Sumworks.co.uk - front page and content page design
Site design for Sumworks.co.uk - a UK site hosting different calculators
Creative Brief
Internet Services
http://www.plotmeadow.co.uk
Project: Sumworks.co.uk
Idea: To host all of the different types of calculators on the site with supporting content
Our idea is generating targeted traffic through generic domains (we've got 4,500!). With Sumworks.co.uk, the domain will host loads of different calculators with content supporting the calculators on offer.
For Sumworks.co.uk, we'd like a design that is clean but colourful and allows us to colour the different sections of the site that we'll have. The initial premise is that we'll have sections for the different 'types' of calculators:
Health calculators
Finance calculators
Maths calculators
Conversion calculators
Pregnancy calculators
Within each section will be different calculators - so, for example, in Health, there will be a BMI calculator, BMR calculator and so on.
Ideally, we'd like each 'section' to have a different colour - i.e. blue for Health, green for Finance, blue for Maths, etc. The colours can be chosen by the designer as to what looks best.
We'd like a front page design and also a content page design. The home page shouldn't be too different in structure/layout to the content pages (i.e. structure follows through).
Ideally, there will be a column on the right hand side that allows advertising (300 x 250) and the main column for content should be at least 540px (this is where content and weidgets/calculators will be placed).
Once in a section, there should be a left menu that allows users to choose the type of calculator they want within that section.
This is our first try on Pixelgrove and we're hoping that if this works out, we can find some designer(s) through this who we can offer many more design projects as we have many generic domain names waiting to be designed.
Likes: Clean, colourful, elegant, professional
www.vitalpage.com
http://www.brightjotapp.com/tour/why-use-brightjot
http://www.kelvo.com/

```html
<!DOCTYPE html>
<html lang="en">
<head>
<meta charset="utf-8">
<title>Sumworks.co.uk – Health Calculator</title>
<link href="https://fonts.googleapis.com/css2?family=Arimo:wght@400;700&display=swap" rel="stylesheet">
<style>
:root{
  --ink:#333;
  --navy:#1f3a4d;
  --navy-dark:#172d3c;
  --teal:#1f4f66;
  --teal-light:#2e6a85;
  --orange:#f7931e;
  --orange-dark:#e0760a;
  --green:#8cc63f;
  --green-dark:#6ea52a;
  --grey-bar:#e4e6e8;
  --page:#ffffff;
  --strip:#eef1f3;
  --link:#2a6fa8;
  --muted:#666;
}
*{margin:0;padding:0;box-sizing:border-box}
html,body{width:1200px;height:722px;overflow:hidden}
body{font-family:"Arimo",Arial,sans-serif;color:var(--ink);background:var(--page);position:relative}
.abs{position:absolute}

.top-nav{left:0;top:0;width:1200px;height:22px;background:var(--navy)}
.top-nav ul{list-style:none;position:absolute;left:168px;top:0;display:flex}
.top-nav li{color:#fff;font-size:11px;line-height:22px;padding:0 13px;border-right:1px solid #33566d}
.top-nav li.active{background:var(--navy-dark)}
.top-util{right:168px;top:0;color:#fff;font-size:10px;line-height:22px}

.header{left:0;top:22px;width:1200px;height:74px;background:linear-gradient(#fff,#f2f4f5);border-bottom:1px solid #dde2e5}
.brand{left:172px;top:42px;display:flex;align-items:center;gap:8px}
.brand-mark{width:24px;height:24px;background:var(--navy)}
.brand-name{font-size:38px;font-weight:700;color:var(--navy);letter-spacing:-1px}
.search{left:816px;top:60px;width:204px;height:19px;border:1px solid #c9d0d5;border-radius:10px;background:#fff;font-size:9px;color:#999;padding:4px 10px}
.search-btn{right:-1px;top:-1px;width:24px;height:19px;border-radius:0 10px 10px 0;background:var(--orange)}

.side-nav{left:173px;top:100px;width:110px}
.side-nav a{display:flex;align-items:center;justify-content:center;text-align:center;height:50px;margin-bottom:5px;color:#fff;font-size:12px;line-height:14px;text-decoration:none;background:linear-gradient(var(--teal-light),var(--teal));border-radius:3px}
.side-nav a.current{background:linear-gradient(#fbab40,var(--orange-dark));position:relative}
.side-nav a.current::after{content:"";position:absolute;right:-10px;top:18px;border:7px solid transparent;border-left:10px solid var(--orange-dark);border-right:0}

.calc{left:293px;top:100px;width:463px;height:262px;background:#fff}
.calc h2{position:absolute;left:14px;top:14px;font-size:17px;color:#222}
.unit-bar{height:19px;background:var(--grey-bar);font-size:12px;padding:3px 8px;color:#444}
.or{font-size:12px;font-weight:700;color:#444}
.lbl{font-size:10px;color:#666}
.field{height:13px;background:#f2f2f2;border:1px solid #e0e0e0}
.btn{height:22px;border-radius:3px;background:linear-gradient(#a6d95c,var(--green-dark));color:#fff;font-size:11px;text-align:center;line-height:22px}

.ad-main{left:768px;top:125px;width:264px;height:187px;background:linear-gradient(160deg,#9ecfea,#e9f4fa 55%,#c9d3d8)}
.ad-main p{position:absolute;left:40px;color:#fff;font-weight:700;text-align:right;right:16px}
.ad-tile{width:114px;height:121px}

.content{left:243px;top:400px;width:515px}
.content h1{font-size:21px;font-weight:400;color:#1d5f86;border-bottom:2px solid #c8d9e4;padding-bottom:4px;margin-bottom:10px}
.content p{font-size:10.5px;line-height:13px;color:#555;margin-bottom:10px}

.share-band{left:0;top:636px;width:1200px;height:48px;background:var(--strip);border-top:1px solid #dfe4e7}
.share{left:172px;top:649px;display:flex;align-items:center;gap:12px;font-size:8px;color:#777}
.share span.s{display:flex;align-items:center;gap:3px;color:var(--link)}
.share span.s i{display:inline-block;width:9px;height:9px;background:#9aa9b4}
.feed{left:850px;top:648px;display:flex;align-items:center;gap:50px;font-size:9px;color:#444}
.feed .rss-btn{width:58px;height:12px;background:var(--orange);border-radius:2px}
.feed .get{display:flex;align-items:center;gap:5px}
.feed .get i{width:12px;height:12px;background:var(--orange);border-radius:2px}

.footer{left:0;top:686px;width:1200px;height:36px;background:var(--navy)}
.footer-links{left:172px;top:690px;color:#fff;font-size:10px;line-height:13px}
.footer-links b{font-weight:700}
.footer-brand{left:872px;top:690px;color:#fff;font-size:22px;font-weight:700}
</style>
</head>
<body>

<nav class="top-nav abs">
  <ul>
    <li class="active">Home</li><li>About Us</li><li>Services</li><li>Types of Calculator</li><li>Testimonials</li><li>Contact Us</li>
  </ul>
  <div class="top-util abs">Login &nbsp;|&nbsp; Help</div>
</nav>

<header class="header abs"></header>
<div class="brand abs"><span class="brand-mark"></span><span class="brand-name">Sumworks.co.uk</span></div>
<div class="search abs">Search this site<span class="search-btn abs"></span></div>

<nav class="side-nav abs">
  <a class="current">Health<br>Calculators</a>
  <a>Finance<br>Calculators</a>
  <a>Maths<br>Calculators</a>
  <a>Conversion<br>Calculators</a>
  <a>Pregnancy<br>Calculators</a>
</nav>

<section class="calc abs">
  <h2>Enter Your Measurements:</h2>
  <div class="unit-bar abs" style="left:14px;top:63px;width:221px">Standard</div>
  <div class="or abs" style="left:250px;top:58px">OR</div>
  <div class="unit-bar abs" style="left:283px;top:63px;width:168px">Metric</div>

  <div class="lbl abs" style="left:14px;top:104px">Your Height:</div>
  <div class="field abs" style="left:14px;top:121px;width:46px"></div>
  <div class="lbl abs" style="left:68px;top:122px">Feet and</div>
  <div class="field abs" style="left:112px;top:121px;width:46px"></div>
  <div class="lbl abs" style="left:166px;top:122px">Inches</div>

  <div class="lbl abs" style="left:14px;top:160px">Your Weight:</div>
  <div class="field abs" style="left:14px;top:177px;width:84px"></div>
  <div class="lbl abs" style="left:106px;top:178px">Pounds</div>

  <div class="lbl abs" style="left:283px;top:104px">Your Height:</div>
  <div class="field abs" style="left:283px;top:121px;width:80px"></div>
  <div class="lbl abs" style="left:371px;top:122px">Centimeters</div>

  <div class="lbl abs" style="left:283px;top:160px">Your Weight:</div>
  <div class="field abs" style="left:283px;top:177px;width:80px"></div>
  <div class="lbl abs" style="left:371px;top:178px">Kilogram</div>

  <div class="btn abs" style="left:14px;top:214px;width:76px">Calculate</div>
  <div class="btn abs" style="left:98px;top:214px;width:58px">Reset</div>
  <div class="btn abs" style="left:283px;top:214px;width:76px">Calculate</div>
  <div class="btn abs" style="left:367px;top:214px;width:58px">Reset</div>
</section>

<aside>
  <div class="ad-main abs" role="img" aria-label="Car advertisement photo">
    <p style="top:14px;font-size:29px">Ravo is great!</p>
    <p style="top:58px;font-size:17px;line-height:20px">Buy Ravo, because<br>Ravo's so cool!</p>
  </div>
  <div class="ad-tile abs" style="left:774px;top:324px;background:linear-gradient(#f7e7c8,#e8b44a)" role="img" aria-label="Illustrated advertisement banner"></div>
  <div class="ad-tile abs" style="left:912px;top:324px;background:linear-gradient(#e8405a,#f6c330)" role="img" aria-label="Vector graphics advertisement banner"></div>
  <div class="ad-tile abs" style="left:774px;top:455px;background:linear-gradient(#3b3b3b,#1a1a1a)" role="img" aria-label="Software demo advertisement banner"></div>
  <div class="ad-tile abs" style="left:912px;top:455px;background:linear-gradient(#2a2a2a,#3b8fd0)" role="img" aria-label="Training videos advertisement banner"></div>
</aside>

<article class="content abs">
  <h1>Health Calculator</h1>
  <p>Lorem ipsum dolor sit amet, consectetur adipiscing elit. Suspendisse risus est, feugiat vel congue a, volutpat eget ipsum. Vestibulum quis ligula in risus tempus sagittis ac venenatis turpis. Aliquam ullamcorper tristique justo at cursus.</p>
  <p>Sed suscipit, velit vitae blandit aliquet, est lacus blandit quam, in adipiscing dui risus commodo lorem. Nullam lobortis scelerisque sem, euismod imperdiet turpis placerat sit amet.</p>
  <p>Cum sociis natoque penatibus et magnis dis parturient montes, nascetur ridiculus mus. Proin tempus massa sit amet lectus ultrices eget elementum tellus varius. Integer facilisis tellus eu ligula porttitor elementum. Aenean rhoncus ante nec eros congue a hendrerit sapien vehicula.</p>
</article>

<div class="share-band abs"></div>
<div class="share abs">
  <span>Bookmark with:</span>
  <span class="s"><i></i>Tagpile</span>
  <span class="s"><i></i>Upvotr</span>
  <span class="s"><i></i>Findly</span>
  <span class="s"><i></i>Friendbook</span>
  <span class="s"><i></i>Wanderlink</span>
  <span class="s"><i></i>Brightlive</span>
</div>
<div class="feed abs">
  <span class="rss-btn"></span>
  <span class="get"><i></i>Get Latest Feed</span>
</div>

<footer class="footer abs"></footer>
<div class="footer-links abs">Home &nbsp;|&nbsp; About Us &nbsp;|&nbsp; Services &nbsp;|&nbsp; Types of Calculator &nbsp;|&nbsp; Testimonials &nbsp;|&nbsp; Contact Us<br>Copyright 2011, <b>Sumworks.co.uk</b> | All rights reserved.</div>
<div class="footer-brand abs">Sumworks.co.uk</div>

</body>
</html>
```